Brochure Design Project

I need a brochure design for a new start up company based in New Jersey called 'Tarnwick Trading LLC' . It is an import export business, we looking to market couple of import products in USA so we need design that is ready to go to print. we have two products that we want to market, the design can be the same for both. I will need just content added for both products to get two brochures.

I am thinking for A4 single fold ( front, back and two middle pages of size 4" x 5.5" each) brochure design but I am open for creative ideas and therefor any new size that make product and our company stand out and give a clear message to buyers/clients. I am providing full content with some detail requirement so you get better idea about which size will be prefect fit for my products.

Tarnwick's main focus is on import/export of wholesale(i.e large quantity ) products/items shipped in container load(full or partial).
We also have presence in India and Dubai. India is our major manufacturing hub where we have vast network of manufacturer looking to export, Dubai is global import/export hub where we have global import/export agents/distributors connections.

I like to see the design that highlight these items
1. product - product images , title and description is included.
2. our core function - i.e wholesale import/export in container load.. it would be nice to see design with shipping containers,import/export images in the back ground.. the message here is that we only do container load orders.
3. our company - highlighting company's image as a global import/export company - nice to see some images of world map with USA, dubai and india linked or someway clear to show our presence in those places.

Brochure content , product images and logo are attached.

Target Market(s)

wholesale buyers, agents, distributors, importer

Industry/Entity Type

Shipping

Requirements
Must have
• The brochure must include product images(at least 3), company logo, some import export related images (i.e a ship with containers, containers, a import/export port), must not look too busy in terms of content, should be easy to read and clear.
Should not have
• The brochure should not use pattern like z fold brochure. should not use old-style fonts.

```html
<!DOCTYPE html>
<html lang="en">
<head>
<meta charset="utf-8">
<title>Tarnwick Trading LLC – Brochure Spread</title>
<link href="https://fonts.googleapis.com/css2?family=Open+Sans:wght@400;600;700&display=swap" rel="stylesheet">
<style>
  :root {
    --backdrop: #2e2e2e;
    --page-grey: #8d8d8d;
    --page-grey-light: #a4a4a4;
    --page-grey-dark: #5e5e5e;
    --footer-band: #3f3f3f;
    --panel: #e2e2e2;
    --text: #5a5a5a;
    --text-dark: #2f2f2f;
    --heading: #2a2a2a;
    --white: #ffffff;
  }
  * { box-sizing: border-box; margin: 0; padding: 0; }
  html, body { width: 1200px; height: 793px; overflow: hidden; }
  body {
    background: var(--backdrop);
    font-family: "Open Sans", Arial, sans-serif;
    color: var(--text);
  }
  .spread {
    position: absolute; left: 100px; top: 40px;
    width: 1000px; height: 714px;
    background: linear-gradient(180deg, var(--page-grey-light) 0%, var(--page-grey) 55%, var(--page-grey-dark) 100%);
    overflow: hidden;
  }
  .spread::after {
    content: ""; position: absolute; left: 499px; top: 0; width: 2px; height: 100%;
    background: rgba(0,0,0,0.12);
  }
  .hero-photo {
    position: absolute; left: 0; top: 0; width: 730px; height: 255px;
    background: linear-gradient(180deg, #6f7a86 0%, #a9b1b8 45%, #c9cdd0 62%, #4d5f70 66%, #2f4457 100%);
  }
  .product-grid {
    position: absolute; left: 730px; top: 0; width: 270px; height: 255px;
    display: grid; grid-template-columns: 1fr 1fr; grid-template-rows: 1fr 1fr; gap: 4px;
    background: #555;
  }
  .product-tile { width: 100%; height: 100%; }
  .tile-roll   { background: linear-gradient(135deg, #c8c8c8, #8a8e92); }
  .tile-tape   { background: linear-gradient(135deg, #d6e6f2, #2f8fd1); }
  .tile-colour { background: linear-gradient(135deg, #2e6fcf 0%, #e9d321 55%, #1d1d1d 100%); }
  .tile-eyelet { background: linear-gradient(135deg, #3b82d6, #9aa3a8); }

  .brand {
    position: absolute; left: 34px; top: 56px;
    display: flex; align-items: center; gap: 12px;
  }
  .brand-mark { width: 52px; height: 52px; background: var(--white); }
  .brand-name { color: var(--white); font-weight: 600; font-size: 22px; line-height: 1; }
  .brand-url {
    position: absolute; left: 34px; top: 116px;
    color: var(--white); font-size: 9px;
  }

  .footer-band {
    position: absolute; left: 0; bottom: 0; width: 100%; height: 26px;
    background: var(--footer-band);
  }
  .panel {
    position: absolute;
    background: var(--panel);
    box-shadow: 0 1px 3px rgba(0,0,0,0.25);
  }
  .intro { left: 42px; top: 298px; width: 430px; height: 186px; padding: 22px 20px 0 22px; }
  .intro h1 {
    font-size: 10.6px; font-weight: 700; color: var(--heading); text-transform: uppercase;
    white-space: nowrap; margin-bottom: 1px;
  }
  .intro p { font-size: 11.4px; line-height: 1.4; color: var(--text); text-align: justify; }

  .advantages {
    left: 44px; top: 500px; width: 430px; height: 180px; padding: 14px 14px 0 18px;
    display: grid; grid-template-columns: 1fr 1fr; column-gap: 14px;
  }
  .advantage { margin-bottom: 5px; }
  .advantage h2 { font-size: 8px; font-weight: 700; color: var(--text-dark); line-height: 1.2; }
  .advantage p { font-size: 7.9px; line-height: 1.25; color: var(--text); }

  .feature { padding: 18px 16px; font-size: 12.5px; line-height: 1.35; color: var(--text); }
  .feature p + p { margin-top: 12px; }
  .feature-strength { left: 518px; top: 284px; width: 204px; height: 156px; }
  .feature-grommets { left: 734px; top: 284px; width: 230px; height: 156px; }
  .feature-colour   { left: 518px; top: 466px; width: 204px; height: 156px; }
  .feature-specs    { left: 734px; top: 466px; width: 230px; height: 190px; }
</style>
</head>
<body>
  <main class="spread">
    <div class="hero-photo" role="img" aria-label="Container ship loaded with colourful shipping containers, escorted by a tug boat at sea"></div>
    <div class="product-grid">
      <div class="product-tile tile-roll" role="img" aria-label="Rolls of silver tarpaulin sheeting"></div>
      <div class="product-tile tile-tape" role="img" aria-label="Blue and white tarpaulin rolls"></div>
      <div class="product-tile tile-colour" role="img" aria-label="Tarpaulins in blue, yellow and black"></div>
      <div class="product-tile tile-eyelet" role="img" aria-label="Close-up of aluminium grommet on blue tarpaulin"></div>
    </div>

    <div class="brand">
      <span class="brand-mark"></span>
      <span class="brand-name">Tarnwick Trading LLC</span>
    </div>
    <span class="brand-url">www.tarnwicktrading.com</span>

    <section class="panel intro">
      <h1>Have you been importing or thinking of importing from overseas?</h1>
      <p>Dealing with overseas suppliers/sellers can be complicated, confusing, time consuming and risky. How about importing from overseas but dealing with someone locally in person? Tarnwick is a New Jersey based import export company. We also have presence in Dubai (a global import/export hub) and India (an emerging production hub of next generation). We bring household and industrial products direct from manufacturers. Our Advantage.</p>
    </section>

    <section class="panel advantages">
      <div>
        <div class="advantage"><h2>1. Direct from Manufacturer</h2><p>We deal direct with manufacturer, no third parties or middleman.</p></div>
        <div class="advantage"><h2>2. Wholesale Container Load (FCL or LCL)<br>Orders</h2><p>Wholesale Container Load order enables manufacturer to provide superior quality at competitive price.</p></div>
        <div class="advantage"><h2>3. Quality Products</h2><p>Our manufacturers have working business relationship with us and have proven track record for supplying the best quality products for many years. Contact us to see original product samples.</p></div>
      </div>
      <div>
        <div class="advantage"><h2>4. Local Contact</h2><p>Dealing with overseas supplier/manufacturer over the phone or internet can be time consuming, confusing and risky at the same time. We are located in Edison New Jersey, from seeing a product sample, requesting a quote to placing an order and tracking shipping you deal with us locally leaving all uncertainty about overseas manufacturer/suppliers.</p></div>
        <div class="advantage"><h2>5. Satisfaction Guarantee</h2><p>We provide 100% satisfaction guarantee on product quality and work with you to facilitate and resolve all logistics, billing and invoicing matters.</p></div>
      </div>
    </section>

    <section class="panel feature feature-strength"><p>- Super Strong, Waterproof, Weather Resistant , Rip-Stop, Tear-Proof, Rot proof</p></section>
    <section class="panel feature feature-grommets"><p>- Rustproof aluminum grommets(eyelets) with sewn-in-welting provides extra strength.</p></section>
    <section class="panel feature feature-colour"><p>- Color: Available in various colors like blue, white, yellow, grey, black, multi-color, and more.</p></section>
    <section class="panel feature feature-specs">
      <p>- Weight/Thickness: 85 gsm (gram per square meter) to 315 gsm or 2.5 oz. per square yard to 9.2 oz. per square yard</p>
      <p>- Size : Available in custom sizes.</p>
      <p>- Manufactured in INDIA</p>
    </section>

    <div class="footer-band"></div>
  </main>
</body>
</html>
```